LotusPEAK yoga mats

Design of the yoga mat boxing. You will find sizing and empty box template in the attached files. We also attached some examples of what style we like from various yoga companies. The design should be minimalistic black / white. Can have geometrics, polygons, mandalas or whatever on it. There should also be a placeholder barcode and some space for the companies name, address and contact.

Our company name:
LotusPEAK
Brennerweg 34
AT- 1230 Vienna

www.lotuspeak-example.eu

```html
<!DOCTYPE html>
<html lang="en">
<head>
<meta charset="utf-8">
<title>LotusPEAK Yoga Mats – Box Dieline</title>
<link href="https://fonts.googleapis.com/css2?family=Montserrat:wght@400;500;600&display=swap" rel="stylesheet">
<style>
  :root {
    --ink: #000000;
    --paper: #ffffff;
    --pattern-dark: #141414;
    --pattern-mid: #5c5c5c;
  }
  * { margin: 0; padding: 0; box-sizing: border-box; }
  html, body { width: 1200px; height: 1000px; overflow: hidden; background: var(--paper); }
  .canvas { position: relative; width: 1200px; height: 1000px; font-family: 'Montserrat', sans-serif; color: var(--ink); }

  .pattern-panel {
    position: absolute; left: 346px; width: 508px;
    background:
      repeating-linear-gradient(90deg, var(--pattern-dark) 0 14px, var(--pattern-mid) 14px 16px),
      var(--pattern-dark);
    background-blend-mode: normal;
  }
  .pattern-panel--top { top: 300px; height: 110px; }
  .pattern-panel--bottom { top: 589px; height: 111px; }

  .side-flap { position: absolute; top: 417px; height: 166px; background: var(--ink); }
  .side-flap--left { left: 231px; width: 110px; }
  .side-flap--right { left: 859px; width: 110px; display: flex; align-items: center; justify-content: center; }

  .flap-brand {
    display: flex; align-items: center; gap: 10px;
    transform: rotate(90deg); color: var(--paper);
    font-size: 12px; font-weight: 500; letter-spacing: 2px; white-space: nowrap;
  }
  .flap-brand .flap-square { width: 22px; height: 22px; border: 1px solid var(--paper); }

  .front-panel {
    position: absolute; left: 346px; top: 417px; width: 508px; height: 166px;
    background: var(--paper); border: 1px solid var(--ink);
  }
  .brand {
    position: absolute; left: 24px; top: 30px; width: 110px;
    display: flex; flex-direction: column; align-items: center; gap: 10px;
  }
  .brand-square { width: 68px; height: 68px; border: 2px solid var(--ink); }
  .brand-name { font-size: 14px; font-weight: 400; letter-spacing: 1.5px; }

  .product-title {
    position: absolute; left: 135px; top: 62px;
    font-size: 27px; font-weight: 500; letter-spacing: 1.5px;
  }
  .address {
    position: absolute; left: 388px; top: 24px;
    font-size: 11px; font-weight: 500; line-height: 14px; font-style: normal;
  }
  .website {
    position: absolute; right: 26px; top: 136px;
    font-size: 10px; font-weight: 600;
  }
</style>
</head>
<body>
<div class="canvas">
  <div class="pattern-panel pattern-panel--top" role="img" aria-label="Black and white geometric star-line pattern covering the box lid"></div>

  <div class="side-flap side-flap--left"></div>

  <section class="front-panel">
    <div class="brand">
      <div class="brand-square"></div>
      <span class="brand-name">LotusPEAK</span>
    </div>
    <h1 class="product-title">YOGA MATS</h1>
    <address class="address">
      LotusPEAK<br>
      Brennerweg 34<br>
      AT- 1230 Vienna
    </address>
    <p class="website">www.lotuspeak-example.eu</p>
  </section>

  <div class="side-flap side-flap--right">
    <div class="flap-brand">
      <span>LotusPEAK</span>
      <span class="flap-square"></span>
    </div>
  </div>

  <div class="pattern-panel pattern-panel--bottom" role="img" aria-label="Black and white geometric star-line pattern covering the box base"></div>
</div>
</body>
</html>
```